Seeking funky, innovative business cards

I am looking to refresh our current business cards to something more engaging, visual and impactful. We are a management consultancy firm, see website (www.larkspur-advisory.com.au). I've included our colour scheme, sample of the slides we use and our old business cards. We would like our cards to have icons. The card should display:- Name- Title- Mobile number- Address- Email address- Website - Company logo- Our purpose statement "We shape workplaces where people truly thrive"

Contact Information for Business Card

Tavish Brellan
Consultant
0491 672 348
Level 5, 218 Warrick Lane, Melbourne 3000
tavish@larkspur-advisory.com.au
www.larkspur-advisory.com.au

Purpose statement "We shape workplaces where people truly thrive"
LOGO available in google images

Font styles to use
Other font styles liked:
• Open Sans Light, Bebas Neue (open to other cool foints)

Colors
ffc214
5c5c5c
f5f5f5
fefefe

Requirements
Must have
• - Name
• - Title
• - Mobile number
• - Address
• - Email address
• - Website
• - Company logo
• - Our purpose statement "We shape workplaces where people truly thrive"
Nice to have
• - Icons
• - Colour (see our colour scheme"

```html
<!DOCTYPE html>
<html lang="en">
<head>
<meta charset="utf-8">
<title>Larkspur Advisory – Business Card</title>
<link href="https://fonts.googleapis.com/css2?family=Lato:ital,wght@0,300;0,400;0,700;1,400&family=Lora:ital@1&display=swap" rel="stylesheet">
<style>
  :root {
    --page: #ffffff;
    --card: #fefefe;
    --ink: #3f4143;
    --charcoal: #474b4c;
    --grey: #5c5c5c;
    --amber: #f5a623;
    --yellow: #ffc214;
    --gold-deep: #d4aa00;
    --gold-warm: #f7a830;
    --tagline: #1f5f9c;
  }
  * { margin: 0; padding: 0; box-sizing: border-box; }
  html, body {
    width: 1200px; height: 1176px; overflow: hidden;
    background: var(--page);
    font-family: "Lato", Arial, sans-serif;
  }
  .card {
    position: absolute; left: 265px; width: 552px; height: 315px;
    border-radius: 18px; overflow: hidden;
  }
  .card-front { top: 212px; background: var(--card); box-shadow: 0 0 0 1px #f0f0f0; }
  .card-back {
    top: 571px;
    background: linear-gradient(35deg, var(--gold-deep) 0%, #e6b21e 50%, var(--gold-warm) 100%);
  }
  .holder-name {
    position: absolute; left: 30px; top: 22px;
    font-size: 22px; font-weight: 400; color: var(--ink); letter-spacing: 0.2px;
  }
  .holder-title {
    position: absolute; left: 31px; top: 50px;
    font-family: "Lora", Georgia, serif; font-style: italic;
    font-size: 13px; color: var(--amber);
  }
  .title-rule {
    position: absolute; left: 31px; top: 81px; width: 24px; height: 4px; background: var(--amber);
  }
  .brand {
    position: absolute; display: flex; align-items: center; gap: 10px;
    font-weight: 300; color: var(--charcoal); white-space: nowrap;
  }
  .brand-dot { border-radius: 50%; background: var(--amber); flex: none; }
  .card-front .brand { right: 30px; top: 86px; font-size: 28px; }
  .card-front .brand-dot { width: 14px; height: 14px; }
  .contact-list { position: absolute; left: 30px; top: 187px; list-style: none; }
  .contact-list li {
    display: flex; align-items: center; height: 23.5px;
    font-size: 13.5px; color: #222;
  }
  .contact-list svg { width: 13px; height: 13px; margin-right: 9px; flex: none; }
  .card-base { position: absolute; left: 0; top: 0; width: 552px; height: 315px; }
  .address {
    position: absolute; left: 30px; top: 268px; height: 18px;
    display: flex; align-items: center; font-size: 13px; color: #fff;
  }
  .address svg { width: 12px; height: 13px; margin-right: 10px; }
  .card-back .brand {
    left: 0; right: 0; top: 138px; justify-content: center;
    font-size: 46px; color: var(--charcoal);
  }
  .card-back .brand-dot { width: 22px; height: 22px; background: #f5f5f5; }
  .purpose {
    position: absolute; left: 0; right: 0; top: 273px; text-align: center;
    font-size: 12.5px; font-weight: 700; color: var(--tagline);
  }
</style>
</head>
<body>

<section class="card card-front" aria-label="Business card front">
  <h1 class="holder-name">Tavish Brellan</h1>
  <p class="holder-title">Consultant</p>
  <div class="title-rule"></div>

  <div class="brand"><span class="brand-dot"></span>Larkspur Advisory</div>

  <ul class="contact-list">
    <li>
      <svg viewBox="0 0 14 14" aria-hidden="true"><path fill="#f5a623" d="M1 5c0-2 2-3 6-3s6 1 6 3v1h-3V5H4v1H1z M3 7h8l1 5H2z"/><circle cx="7" cy="9.5" r="1.5" fill="#fff"/></svg>
      0491 672 348
    </li>
    <li>
      <svg viewBox="0 0 14 14" aria-hidden="true"><rect x="1" y="3" width="12" height="8.5" fill="#f5a623"/><path d="M1.5 3.5 7 8l5.5-4.5" fill="none" stroke="#fff" stroke-width="1.2"/></svg>
      tavish@larkspur-advisory.com.au
    </li>
    <li>
      <svg viewBox="0 0 14 14" aria-hidden="true"><g fill="none" stroke="#f5a623" stroke-width="1"><circle cx="7" cy="7" r="5.5"/><ellipse cx="7" cy="7" rx="2.4" ry="5.5"/><path d="M1.5 7h11M2.5 4h9M2.5 10h9"/></g></svg>
      www.larkspur-advisory.com.au
    </li>
  </ul>

  <svg class="card-base" viewBox="0 0 552 315" aria-hidden="true">
    <defs>
      <linearGradient id="band" x1="0" x2="1">
        <stop offset="0" stop-color="#ffc214"/>
        <stop offset="1" stop-color="#f2a23a"/>
      </linearGradient>
    </defs>
    <path d="M0 269 H350 C338 280 330 286 318 286 H0 Z" fill="url(#band)"/>
    <path d="M0 290 H322 C345 290 352 261 385 261 H552 V315 H0 Z" fill="#474b4c"/>
    <path d="M0 288.5 H322 C345 288.5 352 259.5 385 259.5" fill="none" stroke="#fff" stroke-width="2"/>
  </svg>

  <p class="address">
    <svg viewBox="0 0 12 14" aria-hidden="true"><path fill="#3f4143" d="M6 0a5 5 0 0 1 5 5c0 3.5-5 9-5 9S1 8.5 1 5a5 5 0 0 1 5-5z"/><circle cx="6" cy="5" r="1.8" fill="#ffc214"/></svg>
    Level 5, 218 Warrick Lane,&nbsp; Melbourne 3000
  </p>
</section>

<section class="card card-back" aria-label="Business card back">
  <div class="brand"><span class="brand-dot"></span>Larkspur Advisory</div>
  <p class="purpose">We shape workplaces where people truly thrive</p>
</section>

</body>
</html>
```